furniture and home contents restoration

I need to list the services that we perform in our studio.
we serve the general public as well as the insurance/ remediation industry

```html
<!DOCTYPE html>
<html lang="en">
<head>
<meta charset="utf-8">
<title>Paramount Restorers – Business Card</title>
<link href="https://fonts.googleapis.com/css2?family=Barlow:wght@400;500;600;700;800&display=swap" rel="stylesheet">
<style>
  :root{
    --ink:#24323a;
    --paper:#ffffff;
    --stage:#3a3b3d;
    --muted:#e9edef;
  }
  *{box-sizing:border-box;margin:0;padding:0}
  html,body{width:1200px;height:801px;overflow:hidden}
  body{background:var(--stage);font-family:"Barlow",sans-serif;position:relative}
  .card{position:absolute;width:560px;height:320px;border-radius:12px;overflow:hidden;background:var(--ink);color:var(--paper);box-shadow:0 10px 30px rgba(0,0,0,.35)}
  .card--back{left:28px;top:240px}
  .card--front{left:612px;top:240px}

  /* back */
  .services{display:flex;gap:18px;padding:30px 28px 0 30px;height:228px}
  .services ul{list-style:none;flex:1}
  .services li{font-size:13px;line-height:19.5px;font-weight:500;display:flex;align-items:center;gap:9px;white-space:nowrap}
  .services li::before{content:"";width:0;height:0;border-left:5px solid transparent;border-right:5px solid transparent;border-top:8px solid var(--paper);transform:rotate(-90deg) translateX(0);flex:none}
  .band{position:absolute;left:0;right:0;bottom:0;height:92px;background:var(--paper);color:var(--ink);display:flex;flex-direction:column;justify-content:center;align-items:center;gap:4px}
  .band p{font-size:15px;font-weight:600;letter-spacing:.3px}

  /* front */
  .brand{position:absolute;left:34px;top:62px;font-weight:800;font-size:33px;line-height:32px;letter-spacing:3px;text-transform:uppercase}
  .tagline{position:absolute;left:292px;top:60px;width:250px;text-transform:uppercase}
  .tagline h2{font-size:14px;font-weight:700;letter-spacing:.4px;margin-bottom:4px}
  .tagline p{font-size:11.5px;font-weight:600;line-height:15px;letter-spacing:.3px}
  .person{position:absolute;left:0;right:0;top:150px;text-align:center;font-size:25px;font-weight:700;letter-spacing:1px;text-transform:uppercase}
  .contacts{position:absolute;left:0;right:0;top:200px;display:flex;flex-direction:column;align-items:center;gap:12px;font-size:17px;font-weight:500;letter-spacing:.8px}
  .contacts .row{display:flex;gap:22px;align-items:center}
  .contact{display:flex;align-items:center;gap:7px}
  .contact svg{width:17px;height:17px;fill:var(--paper)}
</style>
</head>
<body>

<section class="card card--back" aria-label="Card back: services">
  <div class="services">
    <ul>
      <li>Antique Repair And Restoration</li>
      <li>Art Cleaning And Remounting</li>
      <li>Art And Mirror Frame Repair</li>
      <li>Chandelier Cleaning And Restoration</li>
      <li>Document Restoration</li>
      <li>Glass, Ceramic, And Mirror Repair</li>
      <li>Hardware Repair And Restoration</li>
      <li>Kitchen Removal And Reinstallation</li>
      <li>Lamp Cleaning And Restoration</li>
      <li>Lamp Shade Replacement</li>
    </ul>
    <ul>
      <li>Metal Polishing And Restoration</li>
      <li>Odor Removal And Ozone Services</li>
      <li>Photo Restoration</li>
      <li>Upholstery Cleaning And Deodorizing</li>
      <li>In-house Upholstery And Reupholstery</li>
      <li>Rug Cleaning And Restoration</li>
      <li>Musical Instrument Restoration</li>
      <li>Window Treatment Repair/ Restoration</li>
      <li>Leather Restoration And Replacement</li>
      <li>Piano Restoration And Repair</li>
    </ul>
  </div>
  <div class="band">
    <p>On-site Inspections And Desk Review Services</p>
    <p>Assessment Reports And Estimates For Repair And Restoration</p>
  </div>
</section>

<section class="card card--front" aria-label="Card front: contact">
  <h1 class="brand">Paramount<br>Restorers</h1>
  <div class="tagline">
    <h2>Home Contents Restoration</h2>
    <p>Serving the general public and the<br>insurance industry for over 40 years</p>
  </div>
  <div class="person">Daniel Moretti</div>
  <div class="contacts">
    <div class="row">
      <span class="contact"><svg viewBox="0 0 24 24"><path d="M6.6 10.8a15 15 0 0 0 6.6 6.6l2.2-2.2c.3-.3.7-.4 1-.2 1.1.4 2.3.6 3.6.6.6 0 1 .4 1 1V20c0 .6-.4 1-1 1A17 17 0 0 1 3 4c0-.6.4-1 1-1h3.5c.6 0 1 .4 1 1 0 1.3.2 2.5.6 3.6.1.3 0 .7-.2 1z"/></svg>555.210.4400</span>
      <span class="contact"><svg viewBox="0 0 24 24"><path d="M7 1h10a2 2 0 0 1 2 2v18a2 2 0 0 1-2 2H7a2 2 0 0 1-2-2V3a2 2 0 0 1 2-2zm0 3v14h10V4zm5 15.5a1 1 0 1 0 0 2 1 1 0 0 0 0-2z"/></svg>555.318.7269</span>
      <span class="contact"><svg viewBox="0 0 24 24"><path d="M6 2h9l3 3v4H6zm-2 8h16a2 2 0 0 1 2 2v7H2v-7a2 2 0 0 1 2-2zm3 6v6h10v-6z"/></svg>555.210.4460</span>
    </div>
    <div class="row">
      <span class="contact"><svg viewBox="0 0 24 24"><path d="M12 2a7 7 0 0 0-7 7c0 5 7 13 7 13s7-8 7-13a7 7 0 0 0-7-7zm0 9.5a2.5 2.5 0 1 1 0-5 2.5 2.5 0 0 1 0 5z"/></svg>82 Birchwood Ave. Riverton, NY 10590</span>
    </div>
    <div class="row">
      <span class="contact"><svg viewBox="0 0 24 24"><path d="M2 5h20v14H2zm2 2v.5l8 5 8-5V7l-8 5z"/></svg>INFO@PARAMOUNTRESTORERS.COM</span>
    </div>
  </div>
</section>

</body>
</html>
```